Velmorak720 is a marketing advisory service company. We provide the following services:
Marketing Strategy
PR and Marketing Communication
Field Marketing
Digital Marketing

We would like to see a design that has either of the following copy:

Everyone can develop a product for the market; not everyone can access the market with the product. Let Velmorak720 help you access the market profitably.

or

Almost every business know how to create value, nor every business can capture value. At Velmorak720, we specialize in helping businesses capture value.

or

It is easy to start a business, attracting and retaining customers and client is the real work. At Velmorak720, we specialize in helping our businesses attract and retain customers and clients.

We can have a slogan that reads:

V-720, your market development partner.....

```html
<!DOCTYPE html>
<html lang="en">
<head>
<meta charset="utf-8">
<title>Velmorak720 – Web Banners</title>
<link href="https://fonts.googleapis.com/css2?family=PT+Sans:wght@400;700&family=Tinos&family=Arimo:wght@700&display=swap" rel="stylesheet">
<style>
  :root {
    --stage-light: #d9d9d9;
    --stage-mid: #8e8e8e;
    --stage-dark: #3a3a3a;
    --banner-deep: #0d3957;
    --banner-mid: #1a5f86;
    --banner-light: #2f7fa6;
    --ink-white: #ffffff;
    --accent-yellow: #f5d800;
    --brand-blue: #1b2f8f;
    --cta-orange: #f04a12;
    --cta-orange-light: #ff7a3c;
    --caption: #f1f1f1;
  }
  * { margin: 0; padding: 0; box-sizing: border-box; }
  html, body { width: 1200px; height: 928px; overflow: hidden; }
  body {
    position: relative;
    font-family: "PT Sans", Arial, sans-serif;
    background:
      radial-gradient(ellipse 900px 520px at 300px 40px, var(--stage-light) 0%, #b8b8b8 45%, transparent 80%),
      linear-gradient(160deg, #c8c8c8 0%, var(--stage-mid) 45%, #5a5a5a 70%, var(--stage-dark) 100%);
  }
  .stage-swoosh { position: absolute; inset: 0; width: 1200px; height: 928px; }

  .banner {
    position: absolute;
    left: 74px;
    width: 1058px;
    height: 142px;
    background: linear-gradient(180deg, var(--banner-light) 0%, var(--banner-mid) 35%, var(--banner-deep) 100%);
    border-bottom: 6px solid #e9e9e9;
    box-shadow: 0 10px 14px rgba(0,0,0,0.45);
  }
  .banner--customers { top: 114px; }
  .banner--value { top: 292px; }
  .banner--access { top: 468px; }

  .brand-box {
    position: absolute;
    left: 6px; top: 6px;
    width: 168px; height: 130px;
    background: var(--ink-white);
    display: flex; flex-direction: column; align-items: center; justify-content: center; gap: 10px;
  }
  .brand-square { width: 62px; height: 62px; background: var(--brand-blue); }
  .brand-name { font-weight: 700; font-size: 20px; color: #222; }

  .pitch {
    position: absolute;
    left: 196px; top: 14px;
    width: 318px;
    color: var(--ink-white);
    font-size: 15px;
    line-height: 19px;
  }
  .pitch em { font-style: normal; color: var(--accent-yellow); font-size: 16px; }

  .visual {
    position: absolute;
    left: 528px; top: 8px;
    width: 150px; height: 126px;
  }

  .tagline {
    position: absolute;
    left: 706px; top: 12px;
    width: 150px;
    text-align: center;
    color: var(--ink-white);
    font-family: "Tinos", "Times New Roman", serif;
  }
  .tagline-code { font-size: 36px; line-height: 40px; }
  .tagline-line { font-size: 20px; line-height: 22px; }

  .chevron { position: absolute; left: 862px; top: 26px; width: 56px; height: 90px; }

  .cta {
    position: absolute;
    left: 936px; top: 26px;
    width: 90px; height: 90px;
    border-radius: 50%;
    background: radial-gradient(circle at 40% 30%, var(--cta-orange-light), var(--cta-orange) 70%);
    border: 2px solid #ffffff;
    color: var(--ink-white);
    font-family: "Arimo", Arial, sans-serif;
    font-weight: 700;
    font-size: 18px;
    line-height: 21px;
    display: flex; align-items: center; justify-content: center; text-align: center;
    text-decoration: none;
  }

  .caption {
    position: absolute;
    left: 262px; top: 818px;
    width: 620px;
    color: var(--caption);
    font-size: 12px;
    line-height: 15px;
  }
</style>
</head>
<body>
  <svg class="stage-swoosh" viewBox="0 0 1200 928" aria-hidden="true">
    <defs>
      <linearGradient id="swoosh" x1="0" y1="0" x2="1" y2="0">
        <stop offset="0" stop-color="#ffffff" stop-opacity="0.55"/>
        <stop offset="0.6" stop-color="#ffffff" stop-opacity="0.15"/>
        <stop offset="1" stop-color="#ffffff" stop-opacity="0"/>
      </linearGradient>
      <linearGradient id="fill-expert" x1="0" y1="0" x2="0" y2="1">
        <stop offset="0" stop-color="#e8f1f8"/>
        <stop offset="1" stop-color="#b9cfe0"/>
      </linearGradient>
      <linearGradient id="fill-values" x1="0" y1="0" x2="0" y2="1">
        <stop offset="0" stop-color="#e9c92a"/>
        <stop offset="1" stop-color="#c9a91a"/>
      </linearGradient>
      <linearGradient id="fill-access" x1="0" y1="0" x2="0" y2="1">
        <stop offset="0" stop-color="#7a55de"/>
        <stop offset="1" stop-color="#5a34c0"/>
      </linearGradient>
    </defs>
    <path d="M0 640 C 260 760, 620 720, 1200 560 L1200 928 L0 928 Z" fill="#2d2d2d" opacity="0.55"/>
    <path d="M0 600 C 260 720, 620 690, 1200 540 L1200 580 C 620 730, 260 770, 0 650 Z" fill="url(#swoosh)"/>
  </svg>

  <section class="banner banner--customers">
    <div class="brand-box"><span class="brand-square"></span><span class="brand-name">Velmorak720</span></div>
    <p class="pitch">It is <em>easy to start</em> a business, attracting and retaining customer and client is the real work. <em>At Velmorak720</em> we <em>specialize</em> in helping our <em>business</em> attract and retain customers and clients.</p>
    <svg class="visual" viewBox="0 0 150 126" role="img" aria-label="Photo of a hand writing the word Expert on a glass board">
      <rect width="150" height="126" fill="url(#fill-expert)"/>
    </svg>
    <div class="tagline"><div class="tagline-code">V-720</div><div class="tagline-line">Your Market Development Partner</div></div>
    <svg class="chevron" viewBox="0 0 56 90" aria-hidden="true"><path d="M4 0 L30 0 L56 45 L30 90 L4 90 L30 45 Z" fill="#ffffff"/></svg>
    <a class="cta" href="#">Learn<br>more</a>
  </section>

  <section class="banner banner--value">
    <div class="brand-box"><span class="brand-square"></span><span class="brand-name">Velmorak720</span></div>
    <p class="pitch"><em>Almost</em> every business know how to create value, <em>Nor</em> every business can capture value. <em>At Velmorak720</em> we specialize in <em>helping business</em> capture value</p>
    <svg class="visual" viewBox="0 0 150 126" role="img" aria-label="Illustration of a road sign reading Core Values">
      <rect width="150" height="126" fill="url(#fill-values)"/>
    </svg>
    <div class="tagline"><div class="tagline-code">V-720</div><div class="tagline-line">Your Market Development Partner</div></div>
    <svg class="chevron" viewBox="0 0 56 90" aria-hidden="true"><path d="M4 0 L30 0 L56 45 L30 90 L4 90 L30 45 Z" fill="#ffffff"/></svg>
    <a class="cta" href="#">Learn<br>more</a>
  </section>

  <section class="banner banner--access">
    <div class="brand-box"><span class="brand-square"></span><span class="brand-name">Velmorak720</span></div>
    <p class="pitch"><em>Everyone</em> can develop a product for the market; <em>Not everyone</em> can access the market with the product. <em>Let Velmorak720</em> help you access the market profitably.</p>
    <svg class="visual" viewBox="0 0 150 126" role="img" aria-label="Illustration of a gear with a figure working at a laptop">
      <rect width="150" height="126" fill="url(#fill-access)"/>
    </svg>
    <div class="tagline"><div class="tagline-code">V-720</div><div class="tagline-line">Your Market Development Partner</div></div>
    <svg class="chevron" viewBox="0 0 56 90" aria-hidden="true"><path d="M4 0 L30 0 L56 45 L30 90 L4 90 L30 45 Z" fill="#ffffff"/></svg>
    <a class="cta" href="#">Learn<br>more</a>
  </section>

  <p class="caption">This is Pixelform's version of Lorem Ipsum. Proin gravida nibh vel velit auctor aliquet. Aenean sollicitudin, lorem quis bibendum auctor, nisi elit consequat ipsum, nec sagittis sem nibh id elit. Duis sed odio sit amet nibh vulputate cursus a sit amet mauris. Morbi accumsan ipsum velit. Nam</p>
</body>
</html>
```